Awesome Business Card Design needed!

Hey there.
I'm looking for a simple but awesome business card design.
Type of company: Online advertisement agency
(please don't use the typical business people or statistics images on the card)
The front has to display the business name
and possibly some sort of logo ( perhaps something with the two M's of the biz name )
And the back of the card should say:
Name
Phone
Email
Let your imagination flow.
here are some designs that I like and that you can use as inspiration.
Simple but Awesome
http://images.pixelvantor.net/designs/55128_877673_43091_thumbnail.jpg
http://images.pixelvantor.net/designs/37714_747642_40106_image.jpg
http://images.pixelvantor.net/designs/55128_877673_43091_image.jpg
http://images.pixelvantor.net/designs/51321_781878_43091_image.jpg
http://images.pixelvantor.net/designs/33378_399063_15912_image.jpg
http://images.pixelvantor.net/designs/2337_271604_9495_image.jpg
good luck

```html
<!DOCTYPE html>
<html lang="en">
<head>
<meta charset="utf-8">
<title>Velora Media — Business Card</title>
<link href="https://fonts.googleapis.com/css2?family=Oswald:wght@500&family=Arimo:wght@400;700&display=swap" rel="stylesheet">
<style>
  :root {
    --stage: #9c9c9c;
    --card-light: #ffffff;
    --card-light-edge: #e4e4e4;
    --ink-dark: #2f2a28;
    --card-dark: #000000;
    --card-dark-border: #3a3a3a;
    --strip-grey: #8e8e8e;
    --brand-blue: #1f5596;
    --accent-blue: #29a3e6;
    --white: #ffffff;
  }
  * { margin: 0; padding: 0; box-sizing: border-box; }
  html, body {
    width: 1200px;
    height: 900px;
    overflow: hidden;
    background: var(--stage);
  }
  .canvas {
    position: relative;
    width: 1200px;
    height: 900px;
  }

  /* Front of card */
  .card-front {
    position: absolute;
    left: 274px;
    top: 60px;
    width: 654px;
    height: 376px;
    background: radial-gradient(ellipse at 50% 45%, var(--card-light) 0%, #f6f6f6 55%, var(--card-light-edge) 100%);
    overflow: hidden;
  }
  .brand {
    position: absolute;
    left: 0;
    right: 0;
    top: 150px;
    display: flex;
    flex-direction: column;
    align-items: center;
    gap: 18px;
  }
  .brand-square {
    width: 28px;
    height: 28px;
    background: var(--brand-blue);
  }
  .brand-name {
    font-family: "Oswald", "Arial Narrow", sans-serif;
    font-weight: 500;
    font-size: 50px;
    line-height: 1;
    letter-spacing: 3px;
    color: var(--ink-dark);
    text-transform: uppercase;
  }
  .front-strip {
    position: absolute;
    left: 0;
    bottom: 0;
    width: 100%;
    height: 12px;
    background: var(--card-dark);
  }

  /* Back of card */
  .card-back {
    position: absolute;
    left: 272px;
    top: 460px;
    width: 658px;
    height: 382px;
    background: var(--card-dark);
    border: 3px solid var(--card-dark-border);
    overflow: hidden;
    font-family: "Arimo", Arial, sans-serif;
    text-align: center;
  }
  .holder-name {
    position: absolute;
    left: 0;
    right: 0;
    top: 133px;
    font-weight: 700;
    font-size: 33px;
    line-height: 1;
    color: var(--white);
    text-decoration: underline;
    text-decoration-thickness: 3px;
    text-underline-offset: 4px;
  }
  .holder-role {
    position: absolute;
    left: 0;
    right: 0;
    top: 176px;
    font-weight: 700;
    font-size: 25px;
    line-height: 1;
    color: var(--accent-blue);
  }
  .contact-list {
    position: absolute;
    left: 0;
    right: 0;
    top: 240px;
    list-style: none;
    font-size: 15px;
    line-height: 30px;
    color: var(--white);
  }
  .contact-label {
    color: var(--accent-blue);
    margin-right: 8px;
  }
  .back-strip {
    position: absolute;
    left: 0;
    bottom: 0;
    width: 100%;
    height: 16px;
    background: var(--strip-grey);
  }

  .strip-accent {
    position: absolute;
    top: 0;
    height: 100%;
    width: 170px;
    background: var(--brand-blue);
  }
  .front-strip .strip-accent { left: 242px; }
  .back-strip .strip-accent { left: 241px; }
</style>
</head>
<body>
  <main class="canvas">
    <section class="card-front" aria-label="Business card front">
      <div class="brand">
        <span class="brand-square" aria-hidden="true"></span>
        <h1 class="brand-name">Velora Media</h1>
      </div>
      <div class="front-strip"><span class="strip-accent"></span></div>
    </section>

    <section class="card-back" aria-label="Business card back">
      <h2 class="holder-name">YOUR NAME</h2>
      <p class="holder-role">CEO</p>
      <ul class="contact-list">
        <li><span class="contact-label">P</span>: 123 456</li>
        <li><span class="contact-label">E</span>: info@VeloraMedia.com</li>
      </ul>
      <div class="back-strip"><span class="strip-accent"></span></div>
    </section>
  </main>
</body>
</html>
```